VOIP company busioness card redesign

Redesign business card to match our new logo and marketing material. Should include logo on one side and contact information on other side.

We like modern and clean

Industry/Entity Type

Phone Company

Contact Information for Business Card

One side should be logo other side should include contact info
Name
Phone Number
email
website

Font styles to use
Other font styles liked:
• dont care

Requirements
Must have
• Modern sleek design that works with our logo

```html
<!DOCTYPE html>
<html lang="en">
<head>
<meta charset="utf-8">
<title>Corvia Business Card</title>
<link rel="stylesheet" href="https://fonts.googleapis.com/css2?family=Roboto:ital,wght@0,400;0,500;0,700;1,400&display=swap">
<style>
  :root {
    --stage: #2c2c2e;
    --brand-blue: #1da3e2;
    --brand-blue-deep: #128fd0;
    --brand-green: #8cc63f;
    --ink: #4a4a4a;
    --paper: #ffffff;
    --paper-shade: #eef1f3;
  }
  * { margin: 0; padding: 0; box-sizing: border-box; }
  html, body { width: 1200px; height: 843px; overflow: hidden; }
  body {
    background: var(--stage);
    font-family: "Roboto", Arial, sans-serif;
    position: relative;
  }
  .card {
    position: absolute;
    left: 260px;
    width: 680px;
    height: 388px;
    border-radius: 4px;
    overflow: hidden;
  }
  .card--back { top: 22px; background: linear-gradient(135deg, var(--brand-blue) 0%, var(--brand-blue-deep) 100%); }
  .card--front { top: 433px; background: linear-gradient(160deg, var(--paper) 55%, var(--paper-shade) 100%); }

  /* back side */
  .back-lockup {
    position: absolute; left: 0; right: 0; top: 140px;
    text-align: center; color: var(--paper);
  }
  .back-lockup .wordmark { font-size: 84px; font-weight: 700; letter-spacing: -1px; line-height: 1; }
  .back-url {
    position: absolute; left: 0; right: 0; bottom: 56px;
    text-align: center; color: var(--paper);
    font-size: 14px; letter-spacing: 7px;
  }

  /* front side */
  .identity { position: absolute; left: 46px; top: 110px; }
  .identity .name { color: var(--brand-blue); font-size: 22px; font-weight: 500; }
  .identity .role { color: var(--brand-green); font-size: 18px; font-style: italic; margin-top: 3px; }
  .divider {
    position: absolute; left: 40px; right: 40px; top: 178px;
    height: 2px; background: var(--brand-green);
  }
  .contacts { position: absolute; left: 46px; top: 196px; list-style: none; }
  .contacts li {
    display: flex; align-items: center; gap: 12px;
    color: var(--ink); font-size: 17px; height: 27px;
  }
  .contacts svg { width: 16px; height: 16px; flex: none; }
  .front-lockup { position: absolute; right: 56px; top: 64px; text-align: right; }
  .front-lockup .wordmark {
    color: var(--brand-blue); font-size: 64px; font-weight: 700;
    letter-spacing: -1px; line-height: 1;
  }
  .address {
    position: absolute; right: 56px; top: 252px;
    color: var(--ink); font-size: 17px; line-height: 1.4; text-align: right;
    font-style: normal;
  }
  .edge-stripe { position: absolute; left: 0; right: 0; bottom: 18px; height: 4px; background: var(--brand-green); }
  .edge-band { position: absolute; left: 0; right: 0; bottom: 0; height: 18px; background: var(--brand-blue); }
</style>
</head>
<body>

<section class="card card--back" aria-label="Card back">
  <div class="back-lockup">
    <div class="wordmark">Corvia</div>
  </div>
  <div class="back-url">www.corviavoice.com</div>
</section>

<section class="card card--front" aria-label="Card front">
  <div class="identity">
    <div class="name">Mara Lindqvist</div>
    <div class="role">President</div>
  </div>

  <div class="front-lockup">
    <div class="wordmark">Corvia</div>
  </div>

  <div class="divider"></div>

  <ul class="contacts">
    <li>
      <svg viewBox="0 0 16 16" aria-hidden="true"><path fill="#1da3e2" d="M3.6 1.5l2.2 2.6-1.3 1.6c.9 2 2.6 3.7 4.6 4.6l1.6-1.3 2.6 2.2-1.2 2.3C7.3 15 1 8.7 1.3 2.7z"/></svg>
      <span>555 0142 7788</span>
    </li>
    <li>
      <svg viewBox="0 0 16 16" aria-hidden="true"><rect x="1" y="3" width="14" height="10" rx="1.5" fill="#1da3e2"/><path d="M1.5 4l6.5 5 6.5-5" fill="none" stroke="#fff" stroke-width="1.3"/></svg>
      <span>mara@corviavoice.com</span>
    </li>
    <li>
      <svg viewBox="0 0 16 16" aria-hidden="true"><circle cx="8" cy="8" r="7" fill="#1da3e2"/><path d="M1 8h14M8 1c2.4 2.2 2.4 11.8 0 14M8 1c-2.4 2.2-2.4 11.8 0 14" fill="none" stroke="#fff" stroke-width="1"/></svg>
      <span>www.corviavoice.com</span>
    </li>
  </ul>

  <address class="address">
    2710 Harbor Lane<br>
    Lakeview, NY 10990
  </address>

  <div class="edge-stripe"></div>
  <div class="edge-band"></div>
</section>

</body>
</html>
```